e-commerce website for selling flooring materials and related accessories

We are developing a new e-commerce site based in the US. We plan to sell all types of flooring - such as Hardwood, Laminate, Waterproof flooring and Porcelain tile, marble, Carpet, and related accessories.

OUR BACK END IS MAGENTO 2.

Target Market(s)

consumer, builder & contractors, hospitality industry, architect, designers, private sector

Industry/Entity Type

Flooring

Coding

Coded - Design and coding required

Number of Pages Required

5+ page

Font styles to use
Sans Serif

Requirements
Must have
• Logo placement, 3 Color combination, Banner placement, promotional pricing tags, check out page, blog placement, social media icons, 1800 number, product and related accessories placement. For reference purposes, please visit our competitor websites -
1.www.plankvaultoutlet.net
2.tilehavenhome.com
3.www.grainmarketdepot.com
4.www.craftsupplyhub.com
5.www.mosskeepcorp.com
Nice to have
• Our main customers are women and families and we want to make sure the design is attractive.
we like to have 2 or 3 bands at the top.
please provide design for the bottom page.
Should not have
• As our products are more natural colors, please do not bring extreme colors into the design

```html
<!DOCTYPE html>
<html lang="en">
<head>
<meta charset="utf-8">
<title>Plankora – Flooring Store</title>
<link href="https://fonts.googleapis.com/css2?family=IBM+Plex+Sans:wght@400;500;600;700&display=swap" rel="stylesheet">
<style>
:root{
  --blue:#1b4f9f;
  --blue-deep:#174a92;
  --dark:#2b2b2b;
  --footer:#262626;
  --soft:#f4f1f1;
  --ink:#1d1d1d;
  --muted:#555;
  --orange:#e5481f;
  --white:#fff;
}
*{box-sizing:border-box;margin:0;padding:0}
html,body{width:1200px;height:4019px;overflow:hidden}
body{font-family:"IBM Plex Sans",Arial,sans-serif;color:var(--ink);background:var(--white)}
section,header,footer{position:relative;width:1200px}
.abs{position:absolute}
.ph{position:absolute}
/* header */
.site-header{height:111px}
.brand{position:absolute;left:132px;top:34px;display:flex;align-items:center;gap:12px}
.brand-mark{width:34px;height:34px;background:var(--blue);border-radius:50%}
.brand-name{font-weight:700;font-size:24px;color:var(--ink)}
.search{left:401px;top:22px;width:158px;height:33px;border:1px solid #333;font-size:10px;padding:10px 12px;color:#333}
.search svg{position:absolute;right:8px;top:10px}
.phone{left:583px;top:32px;font-size:15px;font-weight:600;display:flex;gap:6px;align-items:center}
.util{left:723px;top:35px;font-size:10px;color:#333;letter-spacing:.3px}
.util span{margin:0 6px}
.cart-badge{display:inline-block;width:14px;height:14px;border-radius:50%;background:var(--blue);color:#fff;font-size:8px;text-align:center;line-height:14px;vertical-align:top}
.main-nav{left:400px;top:77px;display:flex;gap:24px;font-size:12px;font-weight:500;letter-spacing:.2px}
.main-nav li{list-style:none}
.main-nav li::after{content:" ⌵";font-size:10px}
.main-nav .active{color:var(--blue)}
/* hero */
.hero{height:489px;background:linear-gradient(180deg,#8a6a4a 0%,#b87a3e 45%,#d89a55 75%,#c77a3a 100%)}
.hero-tag{left:133px;top:294px;width:368px;height:110px;background:rgba(110,110,110,.72);padding:12px 16px;color:#fff}
.hero-tag h1{font-size:46px;font-weight:700;letter-spacing:1px;line-height:1.05}
.hero-tag p{font-size:13.5px;font-weight:700;line-height:1.35;margin-top:6px}
/* section titles */
.sec-title{position:absolute;left:0;width:1200px;text-align:center;font-size:19px;font-weight:700;letter-spacing:.3px}
.sec-title span{display:inline-flex;align-items:center;gap:14px}
.sec-title span::before,.sec-title span::after{content:"";width:36px;height:3px;background:var(--blue)}
/* styles grid */
.styles{height:570px}
.style-grid{left:132px;top:120px;display:grid;grid-template-columns:repeat(4,225px);grid-auto-rows:194px;gap:8px 10px}
.style-tile{position:relative}
.style-tile b{position:absolute;left:14px;bottom:12px;color:#fff;font-size:11px;letter-spacing:.4px}
.style-tile b::before{content:"";position:absolute;left:0;top:-6px;width:30px;height:2px;background:#fff}
/* features */
.features{height:285px;background:var(--dark);color:#fff}
.feature{position:absolute;top:60px;width:250px;text-align:center}
.feature h3{font-size:16px;font-weight:700;margin-top:20px;letter-spacing:.3px}
.feature p{font-size:12px;line-height:1.35;margin-top:8px;color:#ddd}
.vline{position:absolute;top:55px;width:1px;height:170px;background:#444}
/* sellers */
.sellers{height:448px;background:var(--soft)}
.product{position:absolute;top:130px;width:168px;text-align:center}
.product .img{position:relative;height:168px}
.product .tag{position:absolute;left:2px;top:14px;background:#fff;font-size:8.5px;padding:1px 3px}
.product p{font-size:12.5px;font-weight:600;line-height:1.3;margin-top:17px}
.product strong{display:block;color:var(--blue);font-size:15px;margin-top:10px}
.arrow{position:absolute;font-size:26px;color:#888}
/* offers */
.offers{height:462px}
.offer{position:absolute;top:125px;width:302px;height:277px}
.offer-bar{position:absolute;left:0;top:190px;width:7px;height:82px;background:#fff}
.offer h4{position:absolute;left:23px;bottom:18px;color:#fff;font-size:13.5px;line-height:1.22;letter-spacing:.4px}
.discount{position:absolute;right:0;bottom:0;width:104px;height:84px;background:var(--blue);border-radius:60px 0 0 0;color:#fff;text-align:center;padding-top:20px}
.discount small{font-size:10px;text-decoration:underline}
.discount div{font-size:28px;font-weight:700;line-height:1}
.discount div sup{font-size:13px}
/* testimonials */
.testimonials{height:380px;background:linear-gradient(90deg,#1a4a92,#1e55a6 50%,#1a4a92);color:#fff}
.testimonials .sec-title span::before,.testimonials .sec-title span::after{background:#3a73c8}
.quote{position:absolute;top:129px;width:453px;height:192px;border:2px solid #fff;padding:30px 40px 0 44px;font-size:12.5px;line-height:1.3}
.quote .q1{position:absolute;left:16px;top:10px;font-size:26px;font-weight:700}
.quote .q2{position:absolute;right:14px;bottom:0;font-size:26px;font-weight:700}
.quote .who{position:absolute;left:44px;top:144px;font-weight:700;font-size:12.5px}
.quote .who::before{content:"";position:absolute;left:0;top:-9px;width:20px;height:2px;background:#fff}
/* accessories */
.accessories{height:415px}
.acc-card{left:130px;top:50px;width:937px;height:305px;background:#2f2f2f}
.acc-photo{left:0;top:0;width:540px;height:305px;background:linear-gradient(135deg,#6a4a3a,#a08878 45%,#d6d2cc 70%,#3a3a3a)}
.acc-text{left:576px;top:52px;width:300px;color:#fff}
.acc-text h2{font-size:21px;font-weight:700;letter-spacing:.3px}
.acc-text p{font-size:15px;line-height:1.2;margin-top:16px;color:#e8e8e8}
.btn{display:inline-block;background:var(--orange);color:#fff;font-weight:700;font-size:13px;padding:10px 16px;margin-top:30px;letter-spacing:.3px}
/* blog */
.blog{height:475px;background:var(--soft)}
.post{position:absolute;top:113px;width:225px;height:317px;background:#fff}
.post .img{height:157px}
.post h5{font-size:11.5px;font-weight:700;margin:18px 20px 0;line-height:1.25;letter-spacing:.2px}
.post p{font-size:11px;line-height:1.25;margin:12px 20px 0;color:var(--muted)}
.post .more{display:inline-block;margin:14px 20px 0;background:var(--blue);color:#fff;font-size:9.5px;font-weight:700;padding:4px 10px}
/* footer */
.site-footer{height:384px;background:var(--footer);color:#fff}
.f-brand{left:132px;top:110px;display:flex;align-items:center;gap:12px}
.f-brand .brand-mark{width:34px;height:34px}
.f-col{position:absolute;top:55px}
.f-col h6{font-size:13.5px;font-weight:700;letter-spacing:.4px;margin-bottom:22px}
.f-col li{list-style:none;font-size:12.5px;line-height:21.8px;color:#e6e6e6}
.f-item{display:flex;gap:14px;align-items:flex-start;font-size:12.5px;line-height:1.35;color:#e6e6e6;margin-bottom:22px}
.f-ico{flex:none;width:24px;height:24px;border-radius:50%;background:#fff;display:flex;align-items:center;justify-content:center}
.f-rule{left:132px;top:299px;width:935px;height:1px;background:#444}
.copy{left:0;top:340px;width:1200px;text-align:center;font-size:10.5px;color:#ccc}
</style>
</head>
<body>

<header class="site-header">
  <div class="brand"><div class="brand-mark"></div><div class="brand-name">Plankora</div></div>
  <div class="abs search">SEARCH
    <svg width="11" height="11" viewBox="0 0 12 12"><circle cx="5" cy="5" r="3.8" fill="none" stroke="#222" stroke-width="1.6"/><path d="M8 8l3 3" stroke="#222" stroke-width="1.6"/></svg>
  </div>
  <div class="abs phone">
    <svg width="13" height="13" viewBox="0 0 24 24"><path d="M6.6 10.8a15 15 0 006.6 6.6l2.2-2.2c.3-.3.7-.4 1-.2 1.1.4 2.3.6 3.6.6.6 0 1 .4 1 1V20c0 .6-.4 1-1 1A17 17 0 013 4c0-.6.4-1 1-1h3.5c.6 0 1 .4 1 1 0 1.3.2 2.5.6 3.6.1.3 0 .7-.2 1z" fill="#222"/></svg>
    1800.555.014
  </div>
  <div class="abs util">LOGIN<span>|</span>REGISTER<span>|</span>ORDERS<span>|</span>CONTACT US<span></span><span></span>MY CART
    <svg width="20" height="14" viewBox="0 0 22 16" style="vertical-align:middle"><path d="M1 2h3l2.5 9h11l2-7H6" fill="none" stroke="#333" stroke-width="1.5"/><circle cx="8" cy="14" r="1.3" fill="#333"/><circle cx="16" cy="14" r="1.3" fill="#333"/></svg><span class="cart-badge" style="margin:0">0</span>
  </div>
  <ul class="abs main-nav">
    <li class="active">HARDWOOD</li><li>TILE</li><li>CARPET</li><li>LAMINATE</li><li>VINYL</li><li>AREA RUGS</li><li>COUNTERTOPS</li>
  </ul>
</header>

<section class="hero" role="img" aria-label="Bright open kitchen with glossy hardwood floor and a fireplace">
  <div class="abs hero-tag">
    <h1>HARDWOOD</h1>
    <p>LOREM IPSUM IS SIMPLY DUMMY TEXT OF<br>THE PRINTING AND TYPESETTING INDUSTRY.</p>
  </div>
</section>

<section class="styles">
  <h2 class="sec-title" style="top:53px"><span>SHOP THOUSANDS OF STYLES</span></h2>
  <div class="abs style-grid">
    <div class="style-tile" role="img" aria-label="Hardwood floor" style="background:linear-gradient(180deg,#c9a47a,#a14e1f)"><b>HARDWOOD</b></div>
    <div class="style-tile" role="img" aria-label="Laminate plank samples" style="background:linear-gradient(160deg,#6b6b6b,#5a3b28 60%,#3e2a20)"><b>LAMINATE</b></div>
    <div class="style-tile" role="img" aria-label="Waterproof flooring with water drops" style="background:linear-gradient(150deg,#c4673b,#8a3b1c)"><b>WATERPROOF FLOORING</b></div>
    <div class="style-tile" role="img" aria-label="Bamboo flooring" style="background:linear-gradient(160deg,#5a3a1c,#9b6a32 60%,#7b4f23)"><b>BAMBOO</b></div>
    <div class="style-tile" role="img" aria-label="Marble surface" style="background:linear-gradient(135deg,#c8ccd6,#9aa3b3 50%,#7d8190)"><b>AMARBLE</b></div>
    <div class="style-tile" role="img" aria-label="Carpet texture" style="background:linear-gradient(180deg,#6a6663,#9a9592 50%,#5a5653)"><b>CARPET</b></div>
    <div class="style-tile" role="img" aria-label="Porcelain tile bathroom" style="background:linear-gradient(180deg,#e9e7e3,#bdb9b2)"><b>PORCELAIN TILE</b></div>
    <div class="style-tile" role="img" aria-label="Vinyl plank being laid" style="background:linear-gradient(135deg,#8e8784,#8b6a52 55%,#6a4a36)"><b>VINYL PLANK</b></div>
  </div>
</section>

<section class="features">
  <div class="feature" style="left:86px">
    <svg width="62" height="52" viewBox="0 0 62 52"><rect x="8" y="6" width="46" height="44" fill="none" stroke="#fff" stroke-width="4"/><rect x="18" y="0" width="26" height="8" fill="#fff"/><g fill="#fff"><rect x="15" y="14" width="7" height="6"/><rect x="27" y="14" width="7" height="6"/><rect x="40" y="14" width="7" height="6"/><rect x="15" y="26" width="7" height="6"/><rect x="27" y="26" width="7" height="6"/><rect x="40" y="26" width="7" height="6"/><rect x="26" y="38" width="10" height="12"/><rect x="0" y="46" width="62" height="4"/></g></svg>
    <h3>FREE PICKUP</h3><p>Lorem Ipsum is simply dum<br>my text of the printing and<br>typesetting industry.</p>
  </div>
  <div class="vline" style="left:326px"></div>
  <div class="feature" style="left:331px">
    <svg width="52" height="52" viewBox="0 0 52 52" fill="#fff"><rect x="0" y="0" width="24" height="14"/><rect x="28" y="0" width="24" height="14"/><rect x="0" y="18" width="14" height="14"/><rect x="18" y="18" width="34" height="14"/><rect x="0" y="36" width="30" height="16"/><rect x="34" y="36" width="18" height="16"/></svg>
    <h3>FREE INSTALLATION</h3><p>Lorem Ipsum is simply dum<br>my text of the printing and<br>typesetting industry.</p>
  </div>
  <div class="vline" style="left:596px"></div>
  <div class="feature" style="left:600px">
    <svg width="58" height="56" viewBox="0 0 58 56" fill="#fff"><rect x="2" y="0" width="12" height="44" rx="2"/><path d="M16 40L44 14l8 8-26 26z"/><rect x="2" y="42" width="54" height="14" rx="3"/></svg>
    <h3>FREE SAMPLES</h3><p>Lorem Ipsum is simply dum<br>my text of the printing and<br>typesetting industry.</p>
  </div>
  <div class="vline" style="left:854px"></div>
  <div class="feature" style="left:849px">
    <svg width="80" height="54" viewBox="0 0 80 54" fill="#fff"><rect x="18" y="4" width="36" height="34"/><path d="M56 14h12l10 14v10H56z"/><circle cx="30" cy="44" r="8" stroke="#2b2b2b" stroke-width="3"/><circle cx="66" cy="44" r="8" stroke="#2b2b2b" stroke-width="3"/><rect x="2" y="10" width="12" height="3"/><rect x="0" y="18" width="14" height="3"/><rect x="4" y="26" width="10" height="3"/></svg>
    <h3>$199 DELIVERY</h3><p>Lorem Ipsum is simply dum<br>my text of the printing and<br>typesetting industry.</p>
  </div>
</section>

<section class="sellers">
  <h2 class="sec-title" style="top:55px"><span>TOP SELLERS</span></h2>
  <div class="arrow" style="left:75px;top:195px">‹</div>
  <div class="arrow" style="left:1103px;top:195px">›</div>
  <div class="product" style="left:131px"><div class="img" role="img" aria-label="Dark walnut plank flooring" style="background:linear-gradient(90deg,#3a2516,#5a3a22,#4a2e1a)"><span class="tag">10% OFF</span></div><p>Lorem Ipsum is simply<br>text of the printing</p><strong>$2.50/SFT</strong></div>
  <div class="product" style="left:322px"><div class="img" role="img" aria-label="Honey oak plank flooring" style="background:linear-gradient(90deg,#b5561c,#d9833a,#a8481a)"><span class="tag">10% OFF</span></div><p>Lorem Ipsum is simply<br>text of the printing</p><strong>$2.50/SFT</strong></div>
  <div class="product" style="left:516px"><div class="img" role="img" aria-label="Light ash plank flooring" style="background:linear-gradient(90deg,#cbb79c,#e2d3bd,#c8b398)"><span class="tag">10% OFF</span></div><p>Lorem Ipsum is simply<br>text of the printing</p><strong>$2.50/SFT</strong></div>
  <div class="product" style="left:707px"><div class="img" role="img" aria-label="Medium brown laminate planks" style="background:linear-gradient(135deg,#7a5430,#a57a4c,#6e4a2a)"><span class="tag">10% OFF</span></div><p>Lorem Ipsum is simply<br>text of the printing</p><strong>$2.50/SFT</strong></div>
  <div class="product" style="left:900px"><div class="img" role="img" aria-label="Light grey porcelain tiles" style="background:linear-gradient(135deg,#eef0f1,#cfd4d7)"><span class="tag">10% OFF</span></div><p>Lorem Ipsum is simply<br>text of the printing</p><strong>$2.50/SFT</strong></div>
</section>

<section class="offers">
  <h2 class="sec-title" style="top:55px"><span>SPECIAL OFFERS</span></h2>
  <div class="offer" role="img" aria-label="Room with grey hardwood floor" style="left:130px;background:linear-gradient(180deg,#d8d6d2,#7c6a5c 55%,#4a3a30)"><div class="offer-bar"></div><h4>LOREM IPSUM IS<br>SIMPLY TEXT OF THE<br>PRINTING</h4><div class="discount"><small>STARTING AT</small><div>25%<sup>OFF</sup></div></div></div>
  <div class="offer" role="img" aria-label="Close-up of light wood planks" style="left:448px;background:linear-gradient(180deg,#d6a56a,#c58c4e 50%,#b77a3e)"><div class="offer-bar"></div><h4>LOREM IPSUM IS<br>SIMPLY TEXT OF THE<br>PRINTING</h4><div class="discount"><small>STARTING AT</small><div>50%<sup>OFF</sup></div></div></div>
  <div class="offer" role="img" aria-label="Close-up of grey carpet" style="left:765px;background:linear-gradient(180deg,#5c5856,#938e8a 45%,#6a6562)"><div class="offer-bar"></div><h4>LOREM IPSUM IS<br>SIMPLY TEXT OF THE<br>PRINTING</h4><div class="discount"><small>STARTING AT</small><div>75%<sup>OFF</sup></div></div></div>
</section>

<section class="testimonials">
  <h2 class="sec-title" style="top:60px"><span>TESTIMONIALS</span></h2>
  <div class="arrow" style="left:75px;top:175px;color:#c9d6ee">‹</div>
  <div class="arrow" style="left:1100px;top:175px;color:#c9d6ee">›</div>
  <div class="quote" style="left:130px"><span class="q1">“</span>Sed ut perspiciatis unde omnis iste natus error sit voluptatem accusantium doloremque laudantium, totam rem aperiam, eaque ipsa quae ab illo inventore veritatis et quasi architecto beatae vitae dicta sunt explicabo. Nemo enim ipsam voluptatem quia voluptas sit aspernatur aut odit aut fugit,sed quia consequuntur magni dolores eos qui ration.<span class="who">DANIEL</span><span class="q2">”</span></div>
  <div class="quote" style="left:613px"><span class="q1">“</span>Sed ut perspiciatis unde omnis iste natus error sit voluptatem accusantium doloremque laudantium, totam rem aperiam, eaque ipsa quae ab illo inventore veritatis et quasi architecto beatae vitae dicta sunt explicabo. Nemo enim ipsam voluptatem quia voluptas sit aspernatur aut odit aut fugit,sed quia consequuntur magni dolores eos qui ration.<span class="who">DANIEL</span><span class="q2">”</span></div>
</section>

<section class="accessories">
  <div class="abs acc-card">
    <div class="abs acc-photo" role="img" aria-label="Stacked wood and laminate plank samples on a dark surface"></div>
    <div class="abs acc-text">
      <h2>ACCESSORIES</h2>
      <p>Sed ut perspiciatis unde omnis iste natus error sit voluptatem accusantium dolore mque laudantium, totam rem aperiam, eaque ipsa quae ab illo inventore veritatis et quasi architecto.</p>
      <span class="btn">VIEW ALL COLLECTIONS</span>
    </div>
  </div>
</section>

<section class="blog">
  <h2 class="sec-title" style="top:48px"><span>LATEST BLOG</span></h2>
  <article class="post" style="left:130px"><div class="img" role="img" aria-label="Warm toned hardwood boards" style="background:linear-gradient(135deg,#c8823c,#9a5620)"></div><h5>AT VERO EOS ET ACCUSA<br>MUS ET IUSTO ODIO</h5><p>Sed ut perspiciatis unde omnis iste natus error sit voluptatem accusantium doloremqu.</p><span class="more">READ MORE</span></article>
  <article class="post" style="left:367px"><div class="img" role="img" aria-label="Bright living room with wood floor" style="background:linear-gradient(180deg,#e6e0d4,#a8825a)"></div><h5>AT VERO EOS ET ACCUSA<br>MUS ET IUSTO ODIO</h5><p>Sed ut perspiciatis unde omnis iste natus error sit voluptatem accusantium doloremqu.</p><span class="more">READ MORE</span></article>
  <article class="post" style="left:605px"><div class="img" role="img" aria-label="Empty room with honey wood floor" style="background:linear-gradient(180deg,#d8c9a6,#b07a3e)"></div><h5>AT VERO EOS ET ACCUSA<br>MUS ET IUSTO ODIO</h5><p>Sed ut perspiciatis unde omnis iste natus error sit voluptatem accusantium doloremqu.</p><span class="more">READ MORE</span></article>
  <article class="post" style="left:842px"><div class="img" role="img" aria-label="Laminate floor being installed" style="background:linear-gradient(135deg,#6e6a66,#b89a78 60%,#9c7a56)"></div><h5>AT VERO EOS ET ACCUSA<br>MUS ET IUSTO ODIO</h5><p>Sed ut perspiciatis unde omnis iste natus error sit voluptatem accusantium doloremqu.</p><span class="more">READ MORE</span></article>
</section>

<footer class="site-footer">
  <div class="abs f-brand"><div class="brand-mark"></div><div class="brand-name" style="color:#fff">Plankora</div></div>
  <div class="f-col" style="left:440px"><h6>LINKS</h6>
    <ul><li>CONTACT US</li><li>ABOUT US</li><li>PRIVACY POLICY</li><li>TERMS &amp; CONDITIONS</li><li>INSTALLATION SERVICES</li><li>CAREERS</li><li>BLOG</li></ul>
  </div>
  <div class="f-col" style="left:664px"><h6>CONTACT US</h6>
    <div class="f-item"><span class="f-ico"><svg width="10" height="13" viewBox="0 0 10 14"><path d="M5 0a5 5 0 015 5c0 4-5 9-5 9S0 9 0 5a5 5 0 015-5z" fill="#262626"/><circle cx="5" cy="5" r="1.8" fill="#fff"/></svg></span><span>412 Cedar Grove Lane,<br>Maplewood, FL 30000</span></div>
    <div class="f-item"><span class="f-ico"><svg width="11" height="11" viewBox="0 0 24 24"><path d="M6.6 10.8a15 15 0 006.6 6.6l2.2-2.2c.3-.3.7-.4 1-.2 1.1.4 2.3.6 3.6.6.6 0 1 .4 1 1V20c0 .6-.4 1-1 1A17 17 0 013 4c0-.6.4-1 1-1h3.5c.6 0 1 .4 1 1 0 1.3.2 2.5.6 3.6.1.3 0 .7-.2 1z" fill="#262626"/></svg></span><span>Call Us<br>1800. 555.017.2240</span></div>
    <div class="f-item"><span class="f-ico"><svg width="12" height="9" viewBox="0 0 12 9"><rect width="12" height="9" fill="#262626"/><path d="M0 0l6 5 6-5" fill="none" stroke="#fff" stroke-width="1"/></svg></span><span>E mail Us<br>hello@plankora.com</span></div>
  </div>
  <div class="f-col" style="left:955px"><h6>FOLLOW US</h6>
    <div class="f-item"><span class="f-ico"></span><span>Like us on<br>FRIENDSPACE</span></div>
    <div class="f-item"><span class="f-ico"></span><span>Follow us on<br>CHIRPLINE</span></div>
    <div class="f-item"><span class="f-ico"></span><span>Follow us on<br>WORKLINKS</span></div>
  </div>
  <div class="abs f-rule"></div>
  <div class="abs copy">Copyright © 2020 All Rights Reserved</div>
</footer>

</body>
</html>
```